Redesign of 3-4 page site for professional services firm

Our site is www.kestrelvaleadvisors.com. We currently have a simple page made with HostPlumo tools. But the tools are not able to generate the look and feel we desire. We need a home page similar to current that tells a little about our company, our experience and our team. We need a second page to show details of current and past transactions we have assisted our clients with. Currently this page reads like a word document but we would like for it to present in a cleaner fashion and liven it up with some images that link to the industry served. For example, a motorcycle outline in a circle for the powersports related transactions. We would like page to introduce each member of "Our Team" and highlight their experience with a photo of each person. If there is no photo available, we would like a placeholder to be their initials in a circle that can be updated later. We would also like a contact us section whether this is a different page or part of the home page.

Target Market(s)

Retirement minded business owners

Industry/Entity Type

Professional Services

Coding

Coded - Design and coding required

Requirements
Must have
• See project description. Must include a page or section for "Current Listings" and "Recently Completed Transactions" (can be same page)

```html
<!DOCTYPE html>
<html lang="en">
<head>
<meta charset="utf-8">
<title>Kestrel Vale Advisors — Home</title>
<link rel="stylesheet" href="https://fonts.googleapis.com/css2?family=Montserrat:wght@600;700;800;900&family=Hind:wght@600;700&display=swap">
<style>
  :root {
    --olive: #c4c000;
    --ink: #0a0a0a;
    --crimson: #d2030a;
    --white: #ffffff;
    --mint: #90f28c;
    --coral: #e07575;
    --butter: #ece87e;
    --slate: #333333;
  }
  * { box-sizing: border-box; margin: 0; padding: 0; }
  html, body { width: 1200px; height: 675px; overflow: hidden; background: var(--white); }
  .page { position: relative; width: 1200px; height: 675px; overflow: hidden; font-family: "Montserrat", sans-serif; }

  .brand { position: absolute; left: 30px; top: 60px; display: flex; align-items: center; gap: 10px; }
  .brand-mark { width: 16px; height: 16px; background: var(--olive); }
  .brand-name { font-size: 32px; font-weight: 700; color: var(--slate); letter-spacing: 0.01em; }

  .main-nav { position: absolute; left: 420px; top: 12px; display: flex; align-items: center; height: 24px; }
  .main-nav a { font-size: 8.5px; font-weight: 700; letter-spacing: 0.1em; color: var(--olive); text-decoration: none; padding: 0 6.5px; line-height: 24px; }
  .main-nav a.is-active { background: var(--olive); color: var(--ink); padding: 0 6px 0 8px; margin-right: 1px; }

  .hero { position: absolute; left: 0; top: 68px; width: 1172px; text-align: center; }
  .hero-kicker { font-size: 33px; font-weight: 800; letter-spacing: 0.14em; color: var(--olive); line-height: 38px; margin-left: 20px; }
  .hero-title { margin-top: 11px; font-size: 55px; font-weight: 800; line-height: 59px; color: var(--ink); letter-spacing: 0.005em; }
  .hero-title .accent { color: var(--crimson); }

  .cta { position: absolute; left: 498px; top: 300px; width: 176px; height: 49px; background: var(--olive); color: var(--white); font-family: "Hind", sans-serif; font-weight: 700; font-size: 18px; letter-spacing: 0.12em; display: flex; align-items: center; justify-content: center; padding-left: 6px; text-decoration: none; }

  .pillars { position: absolute; left: 0; top: 396px; width: 1200px; height: 279px; }
  .pillar { position: absolute; top: 0; height: 279px; }
  .pillar--business { left: 0; width: 419px; background: var(--mint); }
  .pillar--transactions { left: 419px; width: 409px; background: var(--coral); }
  .pillar--entrepreneurs { left: 828px; width: 372px; background: var(--butter); }
  .pillar svg { position: absolute; }
  .pillar-label { position: absolute; top: 193px; font-family: "Hind", sans-serif; font-weight: 700; font-size: 27px; letter-spacing: 0.14em; color: var(--white); white-space: nowrap; transform: translateX(-50%); }
</style>
</head>
<body>
<div class="page">
  <div class="brand">
    <span class="brand-mark"></span>
    <span class="brand-name">Kestrel Vale</span>
  </div>

  <nav class="main-nav">
    <a class="is-active" href="#">HOME</a>
    <a href="#">BUSINESS</a>
    <a href="#">LISITINGS</a>
    <a href="#">OUR</a>
    <a href="#">TEAM</a>
  </nav>

  <header class="hero">
    <p class="hero-kicker">WELLCOME</p>
    <h1 class="hero-title">STRATEGICALLY<br>NAVIGATING <span class="accent">BUSINESS</span><br><span class="accent">EXITS</span></h1>
  </header>

  <a class="cta" href="#">GET STARTED</a>

  <section class="pillars">
    <div class="pillar pillar--business">
      <svg style="left:146px;top:70px" width="104" height="110" viewBox="0 0 104 110" fill="none">
        <rect x="1" y="78" width="20" height="30" rx="3" fill="#fff"/>
        <rect x="27" y="64" width="20" height="44" rx="3" fill="#fff"/>
        <rect x="53" y="52" width="20" height="56" rx="3" fill="#fff"/>
        <rect x="79" y="28" width="22" height="80" rx="3" fill="#fff"/>
        <polyline points="3,56 33,34 52,38 86,10" stroke="#fff" stroke-width="6" stroke-linecap="round" stroke-linejoin="round"/>
        <polygon points="76,4 100,0 94,22" fill="#fff"/>
      </svg>
      <span class="pillar-label" style="left:205px">BUSINESS</span>
    </div>

    <div class="pillar pillar--transactions">
      <svg style="left:169px;top:78px" width="88" height="102" viewBox="0 0 88 102" fill="none">
        <rect x="3" y="3" width="51" height="96" rx="8" stroke="#fff" stroke-width="4"/>
        <line x1="18" y1="10" x2="38" y2="10" stroke="#fff" stroke-width="4" stroke-linecap="round"/>
        <line x1="20" y1="91" x2="36" y2="91" stroke="#fff" stroke-width="3" stroke-linecap="round"/>
        <rect x="25" y="33" width="61" height="41" rx="5" fill="#fff"/>
        <rect x="25" y="41" width="61" height="5" fill="#e07575"/>
        <rect x="32" y="55" width="18" height="3" fill="#e07575"/>
        <rect x="32" y="61" width="12" height="3" fill="#e07575"/>
        <rect x="70" y="55" width="7" height="5" fill="#e07575"/>
        <circle cx="26" cy="33" r="16" fill="#fff" stroke="#e07575" stroke-width="3"/>
        <text x="26" y="40" text-anchor="middle" font-family="Montserrat, sans-serif" font-weight="800" font-size="19" fill="#e07575">$</text>
      </svg>
      <span class="pillar-label" style="left:192px">TRANSACTIONS</span>
    </div>

    <div class="pillar pillar--entrepreneurs">
      <svg style="left:147px;top:67px" width="110" height="112" viewBox="0 0 110 112" fill="none" stroke="#fff" stroke-width="3" stroke-linejoin="round" stroke-linecap="round">
        <rect x="33" y="2" width="34" height="30" rx="2"/>
        <polyline points="42,17 48,23 58,11"/>
        <rect x="2" y="32" width="25" height="22" rx="2"/>
        <circle cx="14.5" cy="43" r="3.5"/>
        <rect x="80" y="13" width="25" height="22" rx="2"/>
        <circle cx="92.5" cy="24" r="3.5"/>
        <path d="M50 82 L36 66 Q32 60 38 58 L52 70 L44 34 Q44 28 50 29 Q54 30 55 36 L60 58 L60 50 Q62 45 67 47 Q70 49 70 55 L71 60 Q73 55 77 57 Q80 59 80 64 L81 67 Q84 63 88 66 Q91 69 90 76 L90 88 Q89 96 84 100"/>
        <path d="M60 102 L95 92 L98 102 L64 112 Z"/>
      </svg>
      <span class="pillar-label" style="left:200px">ENTREPRENEURS</span>
    </div>
  </section>
</div>
</body>
</html>
```